Trade Show Banner "Calmwrightery"

1.7' x 3' vertical banner to complement trade show booth panels (3-panel tabletop booth attached). The word file (attached) is for text and not meant to imply design. We manage homeowner and condo associations that are run by volunteer boards of directors who already have full-time jobs or who may have no training in how to run an organization. It can be highly stressful and not very rewarding. We want this poster/banner to convey that feeling of stress along with a hope for relief and relaxation. Our logo is attached. The full logo is the top one in the file. You may also want to use the triangle (attached) in addition to or instead of the logo. Our corporate fonts are attached. Please let me know if you need additional information or if you feel like there is too much copy or any other thoughts or comments you have.

Target Market(s)

Volunteer boards of directors for homeowner and condo associations--all ages, genders, races, occupations.

Industry/Entity Type

Property Management

Other font styles liked:
• "Bright Harbor" is part of a trademark and should be in Mistral with the green from our logo

Requirements
Must have
• Simple, easy to read, don't clash with booth design
Nice to have
• convey the tension of stress contrasted with the feeling of relaxation and relief.

```html
<!DOCTYPE html>
<html lang="en">
<head>
<meta charset="utf-8">
<title>The Art of Calmwrightery</title>
<link rel="stylesheet" href="https://fonts.googleapis.com/css2?family=PT+Sans:ital,wght@0,400;0,700;1,400;1,700&display=swap">
<style>
  :root {
    --sky-top: #8fd6b8;
    --sky-mid: #6fe8c0;
    --sky-low: #5fe6c4;
    --sky-edge: #3fb6d8;
    --cloud: rgba(255, 255, 255, 0.55);
    --ink: #141414;
    --rule: #3a4a44;
    --divider: #1f2f86;
  }
  * { margin: 0; padding: 0; box-sizing: border-box; }
  html, body { width: 680px; height: 1200px; overflow: hidden; }
  body { font-family: "PT Sans", sans-serif; color: var(--ink); }

  .banner {
    position: relative;
    width: 680px;
    height: 1200px;
    overflow: hidden;
  }
  .sky {
    position: absolute;
    inset: 0;
    background:
      radial-gradient(ellipse 260px 70px at 470px 100px, var(--cloud), transparent 70%),
      radial-gradient(ellipse 220px 60px at 170px 150px, var(--cloud), transparent 70%),
      radial-gradient(ellipse 200px 55px at 600px 190px, rgba(255,255,255,0.4), transparent 70%),
      radial-gradient(ellipse 180px 60px at 120px 250px, rgba(255,255,255,0.35), transparent 70%),
      radial-gradient(ellipse 420px 300px at 680px 1200px, var(--sky-edge), transparent 75%),
      linear-gradient(180deg, var(--sky-top) 0%, var(--sky-mid) 35%, var(--sky-low) 70%, #58dcc8 100%);
  }

  .title-kicker {
    position: absolute;
    top: 130px;
    left: 0;
    width: 680px;
    text-align: center;
    font-weight: 700;
    font-size: 36px;
    letter-spacing: 0.5px;
  }
  .title-rule {
    position: absolute;
    top: 188px;
    left: 82px;
    width: 516px;
    height: 1px;
    background: var(--rule);
  }
  .title-main {
    position: absolute;
    top: 190px;
    left: 0;
    width: 680px;
    text-align: center;
    font-weight: 700;
    font-size: 76px;
    line-height: 1.1;
  }

  .relief-list { list-style: none; }
  .relief-item {
    position: absolute;
    left: 30px;
    width: 620px;
    text-align: center;
    font-style: italic;
  }
  .stress {
    font-weight: 700;
    font-size: 21.5px;
    line-height: 1.3;
    letter-spacing: 0.2px;
  }
  .relax {
    font-size: 19.5px;
    line-height: 26px;
    margin-top: 3px;
  }
  .divider {
    position: absolute;
    left: 335px;
    width: 10px;
    height: 10px;
    border-radius: 50%;
    background: var(--divider);
  }

  .company {
    position: absolute;
    top: 1080px;
    left: 0;
    width: 680px;
    display: flex;
    justify-content: center;
    align-items: center;
    gap: 12px;
  }
  .company-mark {
    width: 18px;
    height: 18px;
    background: var(--ink);
  }
  .company-name {
    font-size: 24px;
    font-weight: 400;
    letter-spacing: 0.5px;
    color: var(--ink);
  }
</style>
</head>
<body>
<main class="banner">
  <div class="sky" role="img" aria-label="Soft white clouds drifting in a calm teal sky"></div>

  <h1>
    <span class="title-kicker">THE ART OF</span>
    <span class="title-rule"></span>
    <span class="title-main">Calmwrightery</span>
  </h1>

  <ul class="relief-list">
    <li class="relief-item" style="top:342px">
      <p class="stress">Stress: THE BOARD HAS TOO MUCH WORK TO DO</p>
      <p class="relax">Relax…and let us do the work.</p>
    </li>
    <li class="divider" style="top:420px"></li>

    <li class="relief-item" style="top:458px">
      <p class="stress">Stress: YOUR COMMUNITY HAS “ISSUES.”</p>
      <p class="relax">Relax…and let us give you a Bright Harbor.</p>
    </li>
    <li class="divider" style="top:531px"></li>

    <li class="relief-item" style="top:569px">
      <p class="stress">Stress: YOUR MEMBERS CANNOT PAY ONLINE.</p>
      <p class="relax">Relax…we’ll give your members multiple ways to pay.</p>
    </li>
    <li class="divider" style="top:643px"></li>

    <li class="relief-item" style="top:684px">
      <p class="stress">Stress: COMMUNICATION IS POOR OR INCONSISTENT.</p>
      <p class="relax">Relax…we’ll keep you informed with a robust online portal,<br>chock full of information.</p>
    </li>
    <li class="divider" style="top:788px"></li>

    <li class="relief-item" style="top:826px">
      <p class="stress">Stress: YOUR DELINQUENCIES ARE HIGH.</p>
      <p class="relax">Relax…as a licensed collection agency, we have developed<br>an effective collections program that works in tandem<br>with your collections attorney. Plus, we can report to the<br>credit bureau!</p>
    </li>
  </ul>

  <footer class="company">
    <span class="company-mark"></span>
    <span class="company-name">TALLOW RIDGE MANAGEMENT, INC.</span>
  </footer>
</main>
</body>
</html>
```